Funeral Home needs a tri-fold brochure

We need to have a tri-fold brochure designed for our mortuary. The name of the mortuary is Willowmere Mortuary. The purpose of this brochure is to give consumers and decision makers an easy glimpse into our business.

The brochure will be tri-fold and have full color on both side.(8.5 x 11)

We are not what most people think in terms of a "traditional" funeral home. Do not use anything with a gothic feel. Our logo is light and simple which is how we would like this brochure to also be. The logo is attached. The colors we like are green, gold, white, and black.

Our mortuary offers affordable burial and cremation services. Some key points that we would like noted in brochure are family owned and operated, on-site cremation, and we service all religious faiths.

This is my first time requesting a brochure with ArtFolio, so I'm not sure if I should have text already written or not. I'm open to any questions or suggestions so don't be afraid to ask. I will answer as soon as possible.
Updates

I have just uploaded a scan of an old brochure that the business used that we don't want the new one to look anything like. Also I uploaded a sheet of copy for the features we would like shown on the brochure. Added Wednesday, September 10, 2014

Target Market(s)

decision influencers in churches, hospices, and hospitals. Also families that may be in need of our service.

Industry/Entity Type

Funeral Home

Font styles to use
Serif

Colors
acd036

Requirements
Must have
• My project must have our logo and be a bright brochure.
Should not have
• The project should not have a gothic feel, or use anything that is associated with "traditional" mortuaries like the dove or horse and carriage. No pictures of caskets, urns, or hearses. I have attached a picture of an older brochure that the business has. New design should not look anything like this one.

```html
<!DOCTYPE html>
<html lang="en">
<head>
<meta charset="utf-8">
<title>Willowmere Mortuary – Tri-fold Brochure</title>
<link rel="stylesheet" href="https://fonts.googleapis.com/css2?family=Roboto:wght@300;400;500&display=swap">
<style>
  :root {
    --lime: #8ef000;
    --lime-soft: rgba(190, 255, 90, 0.45);
    --olive: #a0982c;
    --olive-soft: rgba(170, 160, 50, 0.55);
    --white: #ffffff;
  }
  * { margin: 0; padding: 0; box-sizing: border-box; }
  html, body { width: 1200px; height: 933px; overflow: hidden; background: #ffffff; }
  .brochure {
    position: relative; width: 1200px; height: 933px; overflow: hidden;
    font-family: "Roboto", Arial, sans-serif; color: var(--white);
  }
  .backdrop { position: absolute; inset: 0; }
  .block { position: absolute; }
  .title { font-weight: 300; line-height: 1; letter-spacing: -0.5px; white-space: nowrap; }
  .copy { font-size: 15px; line-height: 20px; font-weight: 400; }
  .bullets { list-style: none; }
  .bullets li { position: relative; padding-left: 13px; }
  .bullets li::before { content: "•"; position: absolute; left: 0; }

  .history { left: 44px; top: 38px; width: 340px; }
  .history .title { font-size: 54px; text-align: right; padding-right: 12px; margin-bottom: 12px; }

  .values { left: 44px; top: 262px; width: 340px; }
  .values .title { font-size: 36px; margin-bottom: 14px; }

  .features { left: 428px; top: 478px; width: 345px; }
  .features .title { font-size: 37px; line-height: 46px; margin-bottom: 14px; }
  .features .bullets { font-size: 13.5px; line-height: 17px; }
  .feature-icons { display: flex; gap: 48px; margin: 4px 0 12px 20px; }
  .features .note { font-size: 13.5px; line-height: 17.5px; width: 335px; }
  .features .note + .note { margin-top: 17px; }

  .services { left: 820px; top: 50px; width: 345px; }
  .services .title { font-size: 42px; line-height: 43px; text-align: right; margin-bottom: 22px; }
  .services .title .long { font-size: 37px; }
  .services .bullets { font-size: 13.5px; line-height: 17px; padding-left: 14px; font-weight: 400; }
  .services .faiths { list-style: none; padding-left: 0; }
  .services .faiths li { padding-left: 30px; }
  .services .faiths li::before { content: "o"; left: 10px; }
  .strong { font-weight: 500; }
</style>
</head>
<body>
<div class="brochure">
  <svg class="backdrop" width="1200" height="933" viewBox="0 0 1200 933">
    <defs>
      <linearGradient id="garden" x1="0" y1="0" x2="0" y2="1">
        <stop offset="0" stop-color="#c7d27a"/>
        <stop offset="0.45" stop-color="#6f8f2e"/>
        <stop offset="0.8" stop-color="#a14a35"/>
        <stop offset="1" stop-color="#8a7a3e"/>
      </linearGradient>
      <linearGradient id="canyon" x1="0" y1="0" x2="1" y2="1">
        <stop offset="0" stop-color="#5b3b3e"/>
        <stop offset="0.45" stop-color="#b0685a"/>
        <stop offset="0.6" stop-color="#e8772c"/>
        <stop offset="1" stop-color="#6d4a55"/>
      </linearGradient>
      <linearGradient id="arch" x1="0" y1="0" x2="0" y2="1">
        <stop offset="0" stop-color="#6f9fd6"/>
        <stop offset="0.35" stop-color="#c9d4e2"/>
        <stop offset="0.45" stop-color="#c2632b"/>
        <stop offset="1" stop-color="#9c4a22"/>
      </linearGradient>
    </defs>

    <rect x="0" y="380" width="405" height="553" fill="url(#garden)" role="img" aria-label="Photo of red flowers in a pot beside a small white bicycle in a garden"/>
    <polygon points="0,0 405,0 405,520 200,455 0,540" fill="var(--lime)"/>
    <polygon points="0,450 200,400 405,470 405,520 200,455 0,540" fill="var(--lime-soft)"/>
    <polygon points="0,933 0,858 130,836 405,905 405,933" fill="var(--olive)"/>

    <rect x="405" y="0" width="390" height="480" fill="url(#canyon)" role="img" aria-label="Photo of a narrow sandstone slot canyon glowing orange"/>
    <polygon points="405,330 600,430 795,300 795,470 405,470" fill="var(--olive-soft)"/>
    <polygon points="405,460 600,400 795,470 795,933 405,933" fill="var(--olive)"/>

    <rect x="795" y="380" width="405" height="553" fill="url(#arch)" role="img" aria-label="Photo of a red rock arch in the desert with snowy mountains behind"/>
    <polygon points="795,0 1200,0 1200,500 1000,440 795,520" fill="var(--lime)"/>
    <polygon points="795,420 1000,470 1200,410 1200,500 1000,440 795,520" fill="var(--lime-soft)"/>
    <polygon points="795,933 795,905 1000,860 1200,905 1200,933" fill="var(--olive)"/>
  </svg>

  <section class="block history">
    <h2 class="title">History</h2>
    <p class="copy">Willowmere Mortuary was started in 2001 with the goal of providing an affordable burial and cremation service without cutting corners. Now owned by father and son duo, Walter and Daniel Hale, Willowmere Mortuary is proud to be family owned and operated and a leader in the funeral industry.</p>
  </section>

  <section class="block values">
    <h2 class="title">Willowmere Mortuary</h2>
    <ul class="bullets copy">
      <li>We are not distracted or bound by corporate mandates</li>
      <li>We focus on families, not the bottom line profits for shareholders</li>
      <li>We have an investment in the community</li>
      <li>We have a long term commitment to our business, our families, and our community</li>
    </ul>
  </section>

  <section class="block features">
    <h2 class="title">Features of<br>Willowmere Mortuary</h2>
    <ul class="bullets">
      <li>Affordable services</li>
      <li>On-site Crematory (loved one never leaves our care)</li>
      <li>In-House financing available</li>
    </ul>
    <div class="feature-icons">
      <svg width="76" height="70" viewBox="0 0 76 70" aria-hidden="true">
        <rect x="44" y="6" width="12" height="30" rx="5" fill="#fff" transform="rotate(40 50 21)"/>
        <polygon points="20,30 42,42 30,62 4,66 8,44" fill="#fff"/>
        <path d="M10 66 L16 50 M18 66 L22 52 M26 64 L28 54" stroke="var(--olive)" stroke-width="3"/>
      </svg>
      <svg width="56" height="70" viewBox="0 0 56 70" aria-hidden="true">
        <path d="M28 40 V22 M28 22 C14 22 6 14 6 4 C18 4 28 10 28 22 M28 22 C28 10 38 4 50 4 C50 14 42 22 28 22" stroke="#fff" stroke-width="4" fill="none"/>
        <polygon points="12,40 44,40 40,68 16,68" fill="none" stroke="#fff" stroke-width="4"/>
      </svg>
      <svg width="76" height="70" viewBox="0 0 76 70" aria-hidden="true">
        <polygon points="50,2 72,42 62,42 74,58 26,58 38,42 28,42" fill="#fff"/>
        <rect x="47" y="58" width="6" height="10" fill="#fff"/>
        <polygon points="18,24 32,50 26,50 34,62 2,62 10,50 4,50" fill="#fff"/>
        <rect x="15" y="62" width="6" height="6" fill="#fff"/>
      </svg>
    </div>
    <p class="note">We know there are other funeral homes serving our area, and would never do anything to disparage their services or undermine their success.</p>
    <p class="note">Yet, we need you to know that our funeral home is truly different. We take great pride in the care we provide the families we serve, and invite you to browse this section of our website to learn this simple truth for yourself: the experienced staff of our funeral firm is committed to doing everything we can to meet, and exceed, your expectations.</p>
  </section>

  <section class="block services">
    <h2 class="title">Featured<br>Services of<br><span class="long">Willowmere Mortuary</span></h2>
    <ul class="bullets">
      <li>Cremation services (immediate or with a service)</li>
      <li>Burial Services</li>
      <li>Transportation out of state (ship out)</li>
      <li><span class="strong">Serves all faiths</span>
        <ul class="bullets faiths">
          <li>Catholic</li>
          <li>Protestant</li>
          <li>LDS</li>
          <li>Hindu</li>
          <li>Buddhist</li>
          <li>Non-denominational</li>
        </ul>
      </li>
    </ul>
  </section>
</div>
</body>
</html>
```